Lumora Learning Web Design Project

Who We are:
Lumora Learning is education information portal/ magazine, providing information about the Chinese and International education markets. Our aim is to help school principals improve there curriculum, and parents in understanding this curriculum.

Project Brief:
The site will include education news updates, educational services, curriculum developments and overseas study. We hope the site represents the cross cultural bridge between the west and east. The site will cover both the Sciences and Arts.

Note:
The logo design competition is also underway so we only need the website design

What We want:
This competition is for Design only no coding!
Design a home page based on Template 1,2 or 3. I only need to select one.
The design of an article page.

Optional
Design a Microsoft Windows metro style splash page.

Sites We like:
http://www.kavelin.com.cn/kavelinlingo/default.aspx
http://www.brixtalacademia.co.uk/
http://qrpv.norvatestudio.net/

Template Explanations:
Template 1-
The main information has a dynamic sliding category view that when clicked displays the relevant info.
In addition to the main upper menu it also has a left hand sliding menu that pops out on click or gesture

Template 2-
Has limited number of Articles most of the menus are drop downs from the top menu

Template 3-
No Top menu

Target Market(s)

Teachers, principals and parents

Industry/Entity Type

Education

Requirements
Should not have
• kindergarten preschool feel

```html
<!DOCTYPE html>
<html lang="en">
<head>
<meta charset="utf-8">
<title>Lumora Learning</title>
<link href="https://fonts.googleapis.com/css2?family=Abel&family=Arimo:wght@400;700&display=swap" rel="stylesheet">
<style>
:root{
  --blue:#2a78c4;
  --blue-dark:#1d5fa3;
  --orange:#e0731f;
  --green:#3ba82b;
  --grey:#9b9b9b;
  --grey-light:#e9e9e9;
  --text:#444;
  --footer:#2f2f2f;
  --footer-bar:#3c3c3c;
  --purple:#6a2a8c;
  --menu-orange:#f07a22;
  --menu-blue:#2b73c2;
  --menu-green:#3fae2d;
  --menu-pink:#e2146f;
  --menu-gold:#a9770f;
}
*{box-sizing:border-box;margin:0;padding:0}
html,body{width:818px;height:1200px;overflow:hidden}
body{position:relative;background:#fff;font-family:'Abel',sans-serif;color:var(--text)}
.abs{position:absolute}
.brand{left:102px;top:18px;font-size:27px;color:var(--blue);letter-spacing:-.5px}
.brand small{display:block;font-size:8px;color:#666;text-align:right;margin-top:-4px}
.search{left:532px;top:26px;width:184px;height:21px;border:1px solid #ccc;border-radius:11px;display:flex;align-items:center;font-family:'Arimo',sans-serif}
.search span{flex:1;font-size:6px;color:#aaa;padding-left:9px}
.search b{font-weight:400;font-size:9px;color:#555;border-left:1px solid #ddd;height:100%;display:flex;align-items:center;padding:0 6px;gap:5px;background:#f3f3f3;border-radius:0 11px 11px 0}
.nav{left:0;top:72px;width:818px;height:30px;background:var(--grey-light);border-top:2px solid #bbb;border-bottom:1px solid #ccc}
.nav a{position:absolute;top:0;height:28px;line-height:28px;text-align:center;font-size:11px;color:#333;text-decoration:none;border-right:1px solid #ccc}
.nav a.active{background:var(--blue);color:#fff;top:-3px;height:33px;line-height:36px;border-bottom:3px solid var(--blue-dark)}
.side{left:0;top:100px;width:104px;height:1100px;background:#f1f1f1;border-right:1px solid #ddd}
.side-item{left:3px;width:96px;height:58px;color:#fff;font-size:11px;display:flex;align-items:center;justify-content:center;border-bottom:2px solid rgba(0,0,0,.25)}
.phone{left:8px;top:520px;width:85px;height:156px;border-radius:12px;background:#2a2a2a;border:2px solid #888}
.phone .screen{position:absolute;left:7px;top:22px;width:67px;height:110px;background:#1b1b1b;color:#ddd;font-size:10px;text-align:center;line-height:13px;padding-top:20px}
.phone .screen em{font-style:normal;color:var(--blue);display:block;font-size:10px;margin-top:8px}
.trial{left:0;top:674px;width:103px;height:84px;background:var(--blue);color:#fff;text-align:center;font-size:17px;line-height:20px;padding-top:11px}
.slide{left:124px;top:117px;width:425px;height:207px;background:linear-gradient(120deg,#8c7a6a,#d8c4b4 45%,#e6e1dc 70%,#c47070)}
.caption{left:116px;top:324px;width:442px;height:31px;background:var(--blue);color:#fff;font-size:17px;line-height:31px;padding-left:10px}
.dots{right:12px;top:11px;display:flex;gap:4px}
.dots i{width:9px;height:9px;border-radius:50%;background:#fff}
.dots i:first-child{background:#4a2f7a}
.bar{left:116px;width:442px;height:30px;color:#fff;font-size:21px;line-height:30px;padding-left:3px}
.cat{top:370px;background:var(--orange);border-bottom:2px solid #b85a12}
.cat .pager{right:4px;top:9px;display:flex;gap:4px}
.cat .pager i{width:10px;height:10px;border-radius:50%;background:#fff}
.cols{font-size:10.5px;line-height:20.5px;color:#444}
.rule{left:116px;width:442px;height:3px;border-top:1px dashed #ddd;border-bottom:1px solid #eee}
.region{left:116px;width:442px;height:27px;color:#fff;font-size:19px;display:flex;justify-content:space-between;align-items:center;padding:0 6px}
.news{top:778px;background:var(--green);border-bottom:3px solid #2a7d1e}
.news .blog{right:8px;top:0;font-size:11px}
.thumb{top:833px;width:136px;height:86px}
.news-text{top:928px;font-size:11.5px;line-height:21px;color:#444;width:140px}
.panel{left:568px;width:147px;border:1px solid #ddd;background:#fff}
.fb{top:116px;height:186px;font-family:'Arimo',sans-serif;font-size:7px;color:#333}
.fb h4{background:#eee;font-size:8px;padding:5px 6px;border-bottom:1px solid #ddd}
.fb .icon{left:6px;top:28px;width:24px;height:24px;background:#3b5a98}
.fb .name{left:38px;top:28px;font-size:9px;font-weight:700;color:#3b5a98}
.fb .like{left:38px;top:41px;border:1px solid #ccc;background:#f3f3f3;padding:1px 4px;font-size:6px}
.fb .count{left:6px;top:65px}
.fb .faces{left:6px;top:75px;display:grid;grid-template-columns:repeat(4,32px);gap:3px 3px}
.fb .faces div{height:32px;background:#8d8f94;position:relative}
.fb .faces span{position:absolute;bottom:-9px;left:0;width:32px;text-align:center;font-size:5.5px;color:#6078a8}
.fb .plugin{left:6px;bottom:4px;font-size:5.5px;color:#6078a8}
.ph{font-size:21px;color:var(--blue);padding:12px 10px 6px;border-bottom:3px solid #ccc}
.tw{top:311px;height:235px}
.tw .bird{display:inline-block;width:30px;height:30px;border-radius:50%;background:#3a8fd8;vertical-align:middle;margin-right:6px}
.tweet{display:flex;gap:8px;padding:8px 8px 0;font-family:'Arimo',sans-serif;font-size:6px;line-height:11px;color:#333}
.tweet .av{width:30px;height:30px;background:#ddd;flex:none}
.tweet b{font-size:6.5px}
.scroll{right:4px;width:2px;background:var(--blue)}
.jobs{top:556px;height:278px}
.job{height:52px;display:flex;align-items:center;justify-content:center;gap:5px;font-family:'Arimo',sans-serif;font-size:9px;font-weight:700;color:#2a3d7a;text-align:center;line-height:10px}
.job i{width:10px;height:10px;border-radius:50%;background:#2a3d7a;flex:none}
.ad{left:569px;top:845px;width:145px;height:152px;background:var(--grey);color:#fff;font-size:14px;display:flex;align-items:center;justify-content:center}
.footer{left:0;top:1007px;width:818px;height:143px;background:var(--footer);color:#ddd}
.footer h3{font-weight:400;font-size:18px;color:#fff;line-height:21px}
.footer p{font-size:11px;line-height:15px}
.footer ul{list-style:none;font-size:11px;line-height:19px}
.footer li::before{content:"";display:inline-block;width:4px;height:4px;background:var(--blue);margin-right:6px;vertical-align:middle}
.signup{left:354px;top:106px;width:124px;height:23px;background:var(--blue);color:#fff;font-size:13px;text-align:center;line-height:22px;border-bottom:2px solid #1a4f8a}
.social{display:flex;gap:4px}
.social i{width:11px;height:11px;border-radius:50%;background:#fff}
.bottom{left:0;top:1150px;width:818px;height:50px;background:var(--footer-bar);color:#fff;text-align:center}
.bottom nav{display:flex;justify-content:center;gap:24px;font-size:11px;padding-top:11px;margin-left:-12px}
.bottom small{display:block;font-size:6.5px;color:#aaa;margin-top:8px;letter-spacing:1px}
</style>
</head>
<body>

<header>
  <div class="abs brand">Lumora Learning<small>some slogan here</small></div>
  <div class="abs search"><span>Enter any Keywords</span><b>SEARCH
    <svg width="8" height="8" viewBox="0 0 8 8"><circle cx="4.5" cy="3.5" r="2.5" fill="none" stroke="#333"/><line x1="2.7" y1="5.3" x2="0.8" y2="7.2" stroke="#333"/></svg></b></div>
</header>

<nav class="abs nav">
  <a class="active" style="left:102px;width:64px">HOME</a>
  <a style="left:166px;width:66px">NEWS</a>
  <a style="left:232px;width:66px">ARTS</a>
  <a style="left:298px;width:80px">SCIENCE</a>
  <a style="left:378px;width:73px">BOOKS</a>
  <a style="left:451px;width:87px">FEATURES</a>
  <a style="left:538px;width:92px">SUBSCRIBE</a>
  <a style="left:630px;width:90px;border:0">CONTACT US</a>
</nav>

<aside class="abs side"></aside>
<div class="abs side-item" style="top:103px;background:var(--purple)">MENU ITEMS</div>
<div class="abs side-item" style="top:165px;background:var(--menu-orange)">MENU ITEMS</div>
<div class="abs side-item" style="top:230px;background:var(--menu-blue)">MENU ITEMS</div>
<div class="abs side-item" style="top:294px;background:var(--menu-green)">MENU ITEMS</div>
<div class="abs side-item" style="top:358px;background:var(--menu-pink)">MENU ITEMS</div>
<div class="abs side-item" style="top:422px;background:var(--menu-gold)">MENU ITEMS</div>

<div class="abs phone"><div class="screen">Get the<br>new app<br>available for<br>tablet &amp; phone<em>Lumora Learning</em></div></div>
<div class="abs trial">FOR A<br>FREE TRIAL<br>CLICK HERE</div>

<main>
  <div class="abs slide" role="img" aria-label="Students seated at a desk listening in class"></div>
  <div class="abs caption">Lorem ipsum dolor sit amet consecutor...
    <div class="abs dots"><i></i><i></i><i></i><i></i></div></div>

  <div class="abs bar cat">Categories<div class="abs pager"><i></i><i></i></div></div>
  <div class="abs cols" style="left:130px;top:415px">Arts<br>Biology &amp; Life Sciences<br>Business &amp; Management<br>Chemistry<br>CS: Artificial Intelligence</div>
  <div class="abs cols" style="left:285px;top:415px">CS: Software Engineering<br>CS: Systems &amp; Security<br>CS: Theory<br>Economics &amp; Finance<br>Education</div>
  <div class="abs cols" style="left:432px;top:417px">Energy &amp; Earth Sciences<br>Engineering<br>Food and Nutrition<br>Health &amp; Society<br>Humanities</div>
  <div class="abs rule" style="top:525px"></div>
  <div class="abs cols" style="left:130px;top:538px;line-height:20.5px">Physical &amp; Earth Sciences<br>Physics<br>Social Sciences<br>Statistics and Data Analysis<br>Teacher Professional<br><span style="line-height:14px;display:block;margin-top:-4px">Development</span></div>
  <div class="abs cols" style="left:287px;top:537px">Information, Tech &amp; Design<br>Law<br>Mathematics<br>Medicine<br>Music, Film, and Audio</div>
  <div class="abs rule" style="top:659px"></div>

  <div class="abs region" style="top:673px;background:var(--grey)"><span>EUROPE</span><span>DRAMA</span></div>
  <div class="abs region" style="top:703px;background:var(--blue)"><span>ASIA</span><span>SCIENCE</span></div>
  <div class="abs region" style="top:732px;background:var(--grey)"><span>USA</span><span>ENGLISH</span></div>

  <div class="abs bar news">Recent News<div class="abs blog">
    <svg width="10" height="10" viewBox="0 0 10 10"><circle cx="1.5" cy="8.5" r="1.3" fill="#f39a1e"/><path d="M1 4.5a4.5 4.5 0 0 1 4.5 4.5M1 1a8 8 0 0 1 8 8" fill="none" stroke="#f39a1e" stroke-width="1.4"/></svg> View Blog</div></div>

  <div class="abs thumb" style="left:118px;background:linear-gradient(135deg,#6b5a4a,#c9a58a 60%,#8b6f5a)" role="img" aria-label="Students gathered around a tablet"></div>
  <div class="abs thumb" style="left:269px;background:linear-gradient(135deg,#6f8aa8,#d7cdb8 55%,#4a6a9a)" role="img" aria-label="Teacher with pupils in a classroom"></div>
  <div class="abs thumb" style="left:420px;background:linear-gradient(135deg,#6f8aa8,#d7cdb8 55%,#4a6a9a)" role="img" aria-label="Teacher with pupils in a classroom"></div>
  <div class="abs news-text" style="left:118px">The Lumora Learning:<br>supporting Education for<br>Everyone</div>
  <div class="abs news-text" style="left:268px">The Lumora Learning:<br>supporting Education for<br>Everyone</div>
  <div class="abs news-text" style="left:419px">The Lumora Learning:<br>supporting Education for<br>Everyone</div>
  <div class="abs rule" style="top:997px"></div>
</main>

<aside>
  <div class="abs panel fb">
    <h4>Find us on Friendwall</h4>
    <div class="abs icon"></div>
    <div class="abs name">Friendwall Platform</div>
    <div class="abs like">Like</div>
    <div class="abs count">2,147,179 people like <b>Friendwall Platform.</b></div>
    <div class="abs faces">
      <div><span>Nadir</span></div><div><span>Rodan</span></div><div><span>Elsa</span></div><div><span>Tomo</span></div>
      <div><span>Kiran</span></div><div><span>Juno</span></div><div><span>Mira</span></div><div><span>Oren</span></div>
    </div>
    <div class="abs plugin">Friendwall social plugin</div>
  </div>

  <div class="abs panel tw">
    <div class="ph"><span class="bird"></span>Chirps</div>
    <div class="tweet"><div class="av"></div><div><b>Marenvale</b> :<br>Lorem ipsum dolor sit amet<br>consecutor. Lorem ipsum.<br>Wed,22 Apr 2013 22 : 33 : 08</div></div>
    <div class="tweet"><div class="av"></div><div><b>Marenvale</b> :<br>Lorem ipsum dolor sit amet<br>consecutor. Lorem ipsum.<br>Wed,22 Apr 2013 22 : 33 : 08</div></div>
    <div class="tweet"><div class="av"></div><div><b>Marenvale</b> :<br>Lorem ipsum dolor sit amet<br>consecutor. Lorem ipsum.<br>Wed,22 Apr 2013 22 : 33 : 08</div></div>
    <div class="abs scroll" style="top:92px;height:100px"></div>
  </div>

  <div class="abs panel jobs">
    <div class="ph">Featured Jobs</div>
    <div style="padding-top:10px">
      <div class="job"><i></i>Harlowe<br>University</div>
      <div class="job"><i></i>Denmoor<br>University</div>
      <div class="job"><i></i>University of<br>Karrow Coast</div>
      <div class="job"><i></i>Ashby<br>University</div>
    </div>
    <div class="abs scroll" style="top:48px;height:170px"></div>
  </div>

  <div class="abs ad">Advertisement</div>
</aside>

<footer class="abs footer">
  <svg class="abs" style="left:104px;top:22px" width="40" height="36" viewBox="0 0 40 36"><rect x="0" y="0" width="28" height="20" fill="#3a9ae0"/><path d="M4 20l0 7 7-7z" fill="#3a9ae0"/><rect x="12" y="9" width="28" height="20" fill="#8bd43a"/><path d="M34 29l0 7-7-7z" fill="#8bd43a"/></svg>
  <h3 class="abs" style="left:162px;top:18px">Have you got an<br>opinion?</h3>
  <p class="abs" style="left:105px;top:69px;width:200px">Why not join in the debate at Lumora Learning and give us your views and opinions on what matters to you!</p>
  <h3 class="abs" style="left:351px;top:18px">Reasons to REGISTER</h3>
  <ul class="abs" style="left:353px;top:43px"><li>Lorem ipsum dolor sit amet</li><li>Lorem ipsum dolor sit amet</li><li>Lorem ipsum dolor sit amet</li></ul>
  <div class="abs signup">SIGN UP NOW</div>
  <div class="abs" style="right:102px;top:18px;font-size:25px;color:var(--blue);text-align:right">Lumora Learning<small style="display:block;font-size:7px;color:#666">some slogan here</small></div>
  <div class="abs" style="right:102px;top:86px;font-size:10px;color:#666">Follow Us On</div>
  <div class="abs social" style="right:102px;top:107px"><i></i><i></i><i></i><i></i></div>
</footer>

<div class="abs bottom">
  <nav><span>HOW TO ADVERTISE</span><span>TERMS &amp; CONDITIONS</span><span>PRIVACY POLICY</span><span>FEEDBACK</span><span>COOKIE POLICY</span><span>HELP</span></nav>
  <small>COPYRIGHT © 2013 Lumora Learning. All Rights Reserved</small>
</div>

</body>
</html>
```